QBrook718 Business Card Design

I am in need of a business card design.

Business Name: Harbor Stone 718 or Qbrook718 (we can try the business card with both variations)

I would like it to be somewhat different from the "average" business card

What do we do?

We link up with distributors of different items and we Market their products, sell their products, fulfill the shipment, and handle all customer service that goes along with it.

I will be uploading our logo as well as other business card ideas that i have seen and liked on the web.

I like the style of the "graphic design" business card that i uploaded. I was thinking maybe something like that but instead would read.

SYNC | SELL | SHIP

With maybe:
a computer or a Sync icon underneath SYNC
Some form of money sign underneath Sell
a delivery truck or something underneath SHIP.

And then I was thinking maybe put the logo on the back side like in the other business card that i uploaded.

I definitely want a double sided business card.

These are only my suggestions and if i was very confident in my idea then I wouldn't have to be on here. (So make what you think is nice because my opinion is probably not so great anyway!!)

Everything can be changed.

ALSO, For the logo
We can try and remove the text multi channel selling

For the Business card contact info:
Tom Haskins
CEO
2419 Pelkey Avenue
J7R-2B8
Montreal, Quebec

Thanks

Target Market(s)

Businesses

Industry/Entity Type

Information Technology

Font styles to use
Serif
Sans Serif
Decorative

Colors
34a6d6
33b8a4
aaaaaa
85cae6
33a6d7
0492cd
9d9d9d

Requirements
Must have
• Double Sided Business card
Nice to have
• Illustration graphics / Icons underneath the main points

```html
<!DOCTYPE html>
<html lang="en">
<head>
<meta charset="utf-8">
<title>Qbrook718 Business Card</title>
<link href="https://fonts.googleapis.com/css2?family=Open+Sans:wght@400;600;700&display=swap" rel="stylesheet">
<style>
  :root {
    --page-bg: #e9e9e9;
    --card-white: #ffffff;
    --brand-blue: #29a9e1;
    --back-blue: #2ba8e0;
    --back-tint: #a6daf2;
    --ink: #3a3a3a;
    --icon-white: #ffffff;
    --divider: rgba(255, 255, 255, 0.45);
  }
  * { margin: 0; padding: 0; box-sizing: border-box; }
  html, body {
    width: 1200px;
    height: 900px;
    overflow: hidden;
    background: var(--page-bg);
    font-family: "Open Sans", Arial, sans-serif;
  }
  .canvas {
    position: relative;
    width: 1200px;
    height: 900px;
  }
  .card {
    position: absolute;
    width: 556px;
    height: 342px;
    overflow: hidden;
    box-shadow: 0 6px 18px rgba(0, 0, 0, 0.12);
  }
  /* Front */
  .card-front {
    left: 238px;
    top: 62px;
    background: var(--card-white);
    color: var(--ink);
  }
  .holder-name {
    position: absolute;
    left: 25px;
    top: 28px;
    font-size: 18px;
    font-weight: 600;
    color: var(--brand-blue);
  }
  .holder-title {
    position: absolute;
    left: 25px;
    top: 54px;
    font-size: 14px;
    font-weight: 400;
  }
  .address {
    position: absolute;
    left: 25px;
    top: 142px;
    font-size: 14px;
    line-height: 20px;
  }
  .contact-list {
    position: absolute;
    left: 25px;
    top: 239px;
    list-style: none;
    font-size: 14px;
    line-height: 20px;
  }
  .contact-list li {
    display: flex;
    align-items: center;
    gap: 6px;
  }
  .contact-list svg { width: 11px; height: 11px; fill: var(--brand-blue); }
  .front-wordmark {
    position: absolute;
    left: 272px;
    top: 148px;
    display: flex;
    align-items: center;
    gap: 8px;
    font-size: 42px;
    line-height: 1;
    font-weight: 700;
    color: var(--brand-blue);
    letter-spacing: -1px;
    white-space: nowrap;
  }
  .wordmark-dot {
    width: 14px;
    height: 14px;
    border-radius: 50%;
    background: var(--brand-blue);
    flex: none;
  }
  /* Back */
  .card-back {
    left: 458px;
    top: 518px;
    width: 560px;
    background: var(--back-blue);
  }
  .back-wordmark {
    position: absolute;
    left: 0;
    right: 0;
    top: 150px;
    display: flex;
    justify-content: center;
    align-items: center;
    gap: 10px;
    font-size: 56px;
    line-height: 1;
    font-weight: 700;
    color: var(--back-tint);
    letter-spacing: -1px;
    white-space: nowrap;
  }
  .back-wordmark .wordmark-dot { background: var(--back-tint); }
  .service-row {
    position: absolute;
    left: 135px;
    top: 262px;
    display: flex;
    align-items: center;
    height: 44px;
  }
  .service-icon {
    width: 82px;
    display: flex;
    justify-content: center;
  }
  .service-icon svg { height: 30px; fill: var(--icon-white); }
  .service-divider {
    width: 1px;
    height: 44px;
    background: var(--divider);
  }
</style>
</head>
<body>
<main class="canvas">
  <section class="card card-front" aria-label="Business card front">
    <h1 class="holder-name">Tom Haskins</h1>
    <p class="holder-title">CEO</p>
    <p class="address">2419 Pelkey Avenue<br>J7R-2B8 Montreal, Quebec</p>
    <ul class="contact-list">
      <li><svg viewBox="0 0 12 12" aria-hidden="true"><path d="M2 1h3l1 3-2 1c.7 1.4 1.6 2.3 3 3l1-2 3 1v3c-5.5 0-10-4.5-10-10z"/></svg>044-987 654 321</li>
      <li><svg viewBox="0 0 12 12" aria-hidden="true"><path d="M0 2h12v8H0z M0 2l6 5 6-5" stroke="#fff" stroke-width="1"/></svg>info@qbrook718.com</li>
      <li><svg viewBox="0 0 12 12" aria-hidden="true"><path d="M5 7l2-2M4 6L2 8a1.4 1.4 0 002 2l2-2M8 6l2-2a1.4 1.4 0 00-2-2L6 4" stroke="#29a9e1" stroke-width="1.5" fill="none"/></svg>www.qbrook718.com</li>
    </ul>
    <div class="front-wordmark"><span class="wordmark-dot"></span>Qbrook718</div>
  </section>

  <section class="card card-back" aria-label="Business card back">
    <div class="back-wordmark"><span class="wordmark-dot"></span>Qbrook718</div>
    <div class="service-row">
      <div class="service-icon" aria-label="Sync">
        <svg viewBox="0 0 32 32" aria-hidden="true"><path d="M16 5a11 11 0 0110 6l3-2v8h-8l3-2.5A7 7 0 009 14H5A11 11 0 0116 5zM16 27a11 11 0 01-10-6l-3 2v-8h8l-3 2.5A7 7 0 0023 18h4a11 11 0 01-11 9z"/></svg>
      </div>
      <span class="service-divider"></span>
      <div class="service-icon" aria-label="Sell">
        <svg viewBox="0 0 20 32" aria-hidden="true"><path d="M9 2h3v3c2.5.4 4.5 1.6 5.5 3.5l-3 1.8C13.8 9 12.4 8.3 10.5 8.3c-2 0-3 .8-3 1.9 0 1.3 1.5 1.8 4 2.5 3.5 1 6 2.3 6 5.8 0 2.8-2 4.7-5.5 5.2V27H9v-3.3c-3-.4-5.2-1.8-6.3-4l3-1.8c.9 1.6 2.6 2.6 4.8 2.6 2.2 0 3.3-.8 3.3-2 0-1.300-1.3-1.8-4-2.6C6.4 15 4 13.8 4 10.5 4 8 5.9 6 9 5.4z"/></svg>
      </div>
      <span class="service-divider"></span>
      <div class="service-icon" aria-label="Ship">
        <svg viewBox="0 0 48 30" aria-hidden="true"><path d="M10 4h24v18H10zM35 9h7l5 7v6H35zM37 11v5h7l-3.5-5z"/><circle cx="17" cy="24" r="4" stroke="#2ba8e0" stroke-width="1.5"/><circle cx="40" cy="24" r="4" stroke="#2ba8e0" stroke-width="1.5"/><path d="M0 8h8M2 12h6M0 16h8" stroke="#fff" stroke-width="1.5"/></svg>
      </div>
    </div>
  </section>
</main>
</body>
</html>
```